Monthly Report PowerPoint Template

We are looking for a set of slides to use as a template for a report that we send out monthly on the state of the solar and storage market. It should be professional and low profile, attached are the slides we currently use/would like to replace: 1) title slide, 2) content summary, 3) content, and 4) section break. We are mainly concerned about a new design for 2), we are using the basic PowerPoint table and would like both a new table style and a version that is more visual. Thanks!

Requirements
Must have
• Light theme
Should not have
• No stock images

```html
<!DOCTYPE html>
<html lang="en">
<head>
<meta charset="utf-8">
<title>Monthly Report Slide Template</title>
<link href="https://fonts.googleapis.com/css2?family=Montserrat:wght@400;500;700;800&display=swap" rel="stylesheet">
<style>
  :root{
    --backdrop:#d4d5e8;
    --navy:#0e4a78;
    --sun:#f5c04a;
    --sky:#dceef8;
    --white:#ffffff;
    --ink:#1b1b1b;
    --bar-top:#ffffff;
    --bar-bottom:#e4e4e4;
  }
  *{box-sizing:border-box;margin:0;padding:0}
  html,body{width:1200px;height:876px;overflow:hidden}
  body{background:var(--backdrop);font-family:'Montserrat',sans-serif;color:var(--ink);position:relative}
  .slide{position:absolute;width:504px;height:310px;background:var(--white);overflow:hidden}
  .slide--title{left:73px;top:85px}
  .slide--summary{left:622px;top:85px}
  .slide--content{left:73px;top:456px}
  .slide--section{left:622px;top:456px;background:var(--sky)}

  .brand{position:absolute;font-family:'Montserrat',sans-serif;font-weight:500;color:var(--navy);letter-spacing:-.3px;white-space:nowrap}
  .brand--lg{left:29px;top:27px;font-size:21px}
  .brand--sm{right:26px;top:23px;font-size:13px}
  .brand--md{left:36px;top:24px;font-size:17px}

  .accent{color:var(--sun)}

  /* title slide */
  .hero-band{position:absolute;left:0;top:79px;width:369px;height:169px;background:var(--sky)}
  .hero-title{position:absolute;left:25px;top:102px;font-size:19.5px;font-weight:800;line-height:21.8px;color:var(--navy);letter-spacing:.2px}
  .hero-lede{position:absolute;left:25px;top:203px;font-size:8.6px;line-height:10.4px;font-weight:500;color:var(--ink)}
  .symbol-area{position:absolute;border-radius:50%;background:radial-gradient(circle at 50% 50%,var(--sun) 0 28%,var(--sky) 30% 100%)}
  .symbol-area--title{left:284px;top:79px;width:170px;height:170px}
  .symbol-area--content{left:309px;top:82px;width:170px;height:170px}

  .url{position:absolute;font-size:8.6px;font-weight:500;color:var(--ink)}
  .slide--title .url{left:25px;top:276px}

  /* section headings */
  .section-head{position:absolute;left:26px;top:27px;font-size:14px;font-weight:800;line-height:15.5px;color:var(--navy);letter-spacing:.3px}

  /* summary rows */
  .toc{position:absolute;left:29px;top:84px;display:grid;grid-template-columns:210px 210px;column-gap:24px;row-gap:15.6px}
  .toc-item{display:flex;align-items:center;height:22px;gap:6px}
  .toc-num{width:18px;height:22px;background:var(--sun);color:var(--white);font-size:9px;font-weight:500;display:flex;align-items:center;justify-content:center}
  .toc-label{flex:1;height:22px;background:linear-gradient(var(--bar-top),var(--bar-bottom));font-size:10px;font-weight:500;display:flex;align-items:center;padding-left:7px;white-space:nowrap}

  /* footers */
  .footer{position:absolute;left:26px;right:26px;top:272px;height:19px;border-top:1.2px solid var(--navy)}
  .footer .url{left:0;top:4px}
  .footer-title{position:absolute;right:22px;top:4px;font-size:8.6px;font-weight:700;letter-spacing:.1px}
  .page-num{position:absolute;right:0;top:0;width:17px;height:18px;background:var(--navy);color:var(--white);font-size:8.6px;display:flex;align-items:center;justify-content:center}

  /* content slide */
  .body-copy{position:absolute;left:26px;top:77px;width:268px;font-size:7px;line-height:12.2px;text-align:justify;color:var(--ink)}
  .body-copy p+p{margin-top:12.2px}

  /* section break */
  .break-title{position:absolute;left:34px;top:114px;font-weight:800;color:var(--navy);letter-spacing:.3px}
  .break-kicker{display:block;font-size:19px;line-height:22px;color:#0d0d0d}
  .break-main{display:block;font-size:25px;line-height:28px}
  .slide--section .url{left:33px;top:289px}
  .section-art{position:absolute;left:300px;top:26px;width:260px;height:340px;border-radius:55% 45% 40% 60%;background:linear-gradient(135deg,var(--navy) 0 30%,var(--sun) 55%,var(--navy) 90%)}
</style>
</head>
<body>

<section class="slide slide--title">
  <div class="brand brand--lg">Volta Insight</div>
  <div class="hero-band"></div>
  <h1 class="hero-title">MARKET<br><span class="accent">INTELLIGENCE</span> FOR<br>THE DISTRIBUTED<br>ENERGY <span class="accent">TRANSITION</span></h1>
  <p class="hero-lede">Volta Insight builds data solutions and publishes<br>research to drive the adoption of clean energy</p>
  <div class="symbol-area symbol-area--title" role="img" aria-label="Brand symbol artwork"></div>
  <div class="url">www.voltainsight.com</div>
</section>

<section class="slide slide--summary">
  <h2 class="section-head">CONTENT<br><span class="accent">SUMMARY</span></h2>
  <div class="brand brand--sm">Volta Insight</div>
  <ol class="toc">
    <li class="toc-item"><span class="toc-num">01</span><span class="toc-label">Content&nbsp; Heading Goes Here</span></li>
    <li class="toc-item"><span class="toc-num">01</span><span class="toc-label">Content&nbsp; Heading Goes Here</span></li>
    <li class="toc-item"><span class="toc-num">01</span><span class="toc-label">Content&nbsp; Heading Goes Here</span></li>
    <li class="toc-item"><span class="toc-num">01</span><span class="toc-label">Content&nbsp; Heading Goes Here</span></li>
    <li class="toc-item"><span class="toc-num">01</span><span class="toc-label">Content&nbsp; Heading Goes Here</span></li>
    <li class="toc-item"><span class="toc-num">01</span><span class="toc-label">Content&nbsp; Heading Goes Here</span></li>
    <li class="toc-item"><span class="toc-num">01</span><span class="toc-label">Content&nbsp; Heading Goes Here</span></li>
    <li class="toc-item"><span class="toc-num">01</span><span class="toc-label">Content&nbsp; Heading Goes Here</span></li>
  </ol>
  <footer class="footer">
    <span class="url">www.voltainsight.com</span>
    <span class="footer-title">RESIDENTIAL AND COMMERCIAL SOLAR</span>
    <span class="page-num">01</span>
  </footer>
</section>

<section class="slide slide--content">
  <h2 class="section-head">HEADING<br><span class="accent">GOES HERE</span></h2>
  <div class="brand brand--sm">Volta Insight</div>
  <div class="body-copy">
    <p>Lorem ipsum dolor sit amet, consectetuer adipiscing elit, sed diam nonummy nibh euismod tincidunt ut laoreet dolore magna aliquam erat volutpat. Ut wisi enim ad minim veniam, quis nostrud exerci tation ullamcorper suscipit lobortis nisl ut aliquip ex ea commodo consequat. Duis autem vel eum iriure dolor in hendrerit in vulputate velit esse molestie consequat, vel illum dolore eu feugiat nulla facilisis at vero eros et accumsan et iusto odio dignissim qui blandit praesent luptatum zzril delenit augue duis dolore te feugait nulla facilisi.</p>
    <p>Lorem ipsum dolor sit amet, cons ectetuer adipiscing elit, sed diam nonummy nibh euismod tincidunt ut laoreet dolore magna aliquam erat volutpat. Ut wisi enim ad minim veniam, quis nostrud exerci tation ullamcorper suscipit lobortis nisl ut aliquip ex ea commodo consequat. Lorem ipsum dolor sit amet, consectetuer adipiscing elit, sed diam nonummy nibh euismod tincidunt ut laoreet dolore magna aliquam</p>
  </div>
  <div class="symbol-area symbol-area--content" role="img" aria-label="Brand symbol artwork"></div>
  <footer class="footer">
    <span class="url">www.voltainsight.com</span>
    <span class="footer-title">RESIDENTIAL AND COMMERCIAL SOLAR</span>
    <span class="page-num">02</span>
  </footer>
</section>

<section class="slide slide--section">
  <div class="brand brand--md">Volta Insight</div>
  <h2 class="break-title"><span class="break-kicker">RESIDENTIAL SOLAR:</span><span class="break-main">MARKET<br>DEMAND TRENDS</span></h2>
  <div class="section-art" role="img" aria-label="Large brand symbol decoration"></div>
  <div class="url">www.voltainsight.com</div>
</section>

</body>
</html>
```